Gestaltung einer Webseite für Eventfotografie
quirlmoos hat hervorragende Arbeit geleistet. Das Design ist 1A, sowie die weitere Projektabwicklung, völlig problemlos, sehr freundlich, entgegenkommend und kompetent. Ich kann quirlmoos jederzeit mit 5 Sternen als Designer weiterempfehlen! gernold
Zielgruppe
Eventagenturen, Entscheider in Marketing- bzw. Eventabteilungen von mittelständischen oder großen Firmen sowie Bankettabteilungen von Hotels.
Aufgabenstellung
Neuerstellung Webseitenlayout und programmtechnische Umsetzung einer Webseite.
Die Webseite soll "Das Glanzstück"heissen. Die Wörter "Das Glanzstück" wären grafisch dementsprechend auch zu gestalten.
Die Webseite dient als Schaufenster zur Generierung von Anfragen / Aufträgen die Eventfotografie betreffend. Da der erste Eindruck entscheidend ist, stelle ich mir beim Aufruf der Webseite vor, dass prominent 3-5 Fotos erscheinen. Die Animation der Fotos soll so gestaltet sein, als wenn man Papierabzüge auf einen Tisch legt (Mein Haus, Mein Pferd, mein Boot...)
Darüber hinaus sollen weitere weniger auffällige Eventfotos erscheinen.
Es sollen eine Homepage, eine Kontaktseite, eine Fotogalerieseite, eine Referenzseite (mit Kundennamen und Fotos) und evtl. ein Onlinekalender integriert sein, auf dem der Benutzer das Eventdatum anklicken und seine Anfrage platzieren kann. Impressum ist obligatorisch.
Alle Bereiche sollen übersichtlich und klar gestaltet sein, so dass sich der User schnell orientieren kann.
Auf jeder Unterseite soll ein ca. 5DM-Stück grosser auffälliger "Termin-Anfrage"-Button platziert sein.

```html
<!DOCTYPE html>
<html lang="de">
<head>
<meta charset="utf-8">
<title>Das Glanzstück – Galerie</title>
<link rel="stylesheet" href="https://fonts.googleapis.com/css2?family=Montserrat:wght@200;300;400&display=swap">
<style>
  :root {
    --bg: #020304;
    --gold: #c9a043;
    --white: #f2f2f2;
    --muted: #1c1f21;
    --glow: rgba(60, 105, 112, 0.28);
    --glow-soft: rgba(45, 80, 88, 0.2);
    --band: #0d0f10;
  }
  * { margin: 0; padding: 0; box-sizing: border-box; }
  html, body { width: 1200px; height: 903px; overflow: hidden; }
  body {
    font-family: "Montserrat", sans-serif;
    position: relative;
    color: var(--white);
    background: var(--bg);
  }

  .backdrop {
    position: absolute; inset: 0;
    background:
      radial-gradient(ellipse 520px 200px at 260px 140px, var(--glow), transparent 70%),
      radial-gradient(ellipse 420px 160px at 180px 300px, var(--glow-soft), transparent 70%),
      radial-gradient(ellipse 560px 200px at 900px 640px, var(--glow-soft), transparent 70%),
      var(--bg);
  }

  .nav { position: absolute; font-size: 14px; letter-spacing: 1.4px; font-weight: 400; white-space: nowrap; line-height: 1; }
  .nav a { color: inherit; text-decoration: none; }
  .nav-primary { left: 210px; top: 147px; color: var(--gold); }
  .nav-secondary { left: 584px; top: 163px; color: var(--white); }

  .brand {
    position: absolute; left: 0; width: 1200px; top: 282px;
    text-align: center; font-weight: 200; font-size: 70px; line-height: 1;
    letter-spacing: 3px; color: var(--white); text-transform: uppercase;
  }

  .strip {
    position: absolute; left: 198px; top: 408px; width: 782px; height: 110px;
    background: linear-gradient(90deg, rgba(40,30,35,0) 0%, #2a2428 12%, #3a3034 50%, #2a2428 88%, rgba(40,30,35,0) 100%);
    opacity: .8;
  }
  .thumbs { position: absolute; left: 226px; top: 449px; display: flex; gap: 17px; }
  .thumb { width: 59px; height: 59px; border: 1px solid #d8d8d8; }

  .caption-band {
    position: absolute; left: 145px; top: 516px; width: 890px; height: 86px;
    background: linear-gradient(90deg, rgba(20,22,24,0) 0%, var(--band) 10%, #141618 50%, var(--band) 90%, rgba(20,22,24,0) 100%);
  }
  .caption {
    position: absolute; left: 0; width: 1200px; top: 566px; text-align: center; line-height: 1;
    font-size: 14px; letter-spacing: 2.6px; font-weight: 300; color: #e0e0e0;
  }

  .page-title {
    position: absolute; left: 97px; top: 758px; font-size: 78px; font-weight: 300; line-height: 1;
    letter-spacing: 9px; color: var(--muted); white-space: nowrap;
  }
</style>
</head>
<body>
  <div class="backdrop" role="img" aria-label="Dunkler Hintergrund mit weichen Lichtschleiern in Petrol"></div>

  <nav class="nav nav-primary">
    <a href="#">HOME</a> | <a href="#">PORTRAIT</a> | <a href="#">GALERIE</a> | <a href="#">REFERENZEN</a>
  </nav>
  <nav class="nav nav-secondary">
    <a href="#">ANFRAGE-KALENDER</a> | <a href="#">KONTAKT</a> | <a href="#">IMPRESSUM</a>
  </nav>

  <h1 class="brand">Das Glanzstück</h1>

  <div class="strip" role="img" aria-label="Unscharfer Streifen mit Eventfotos im Hintergrund"></div>
  <div class="thumbs">
    <div class="thumb" role="img" aria-label="Vorschaubild: Eventdekoration in Pink" style="background:linear-gradient(#c0307a,#5a1038)"></div>
    <div class="thumb" role="img" aria-label="Vorschaubild: Porträtfoto" style="background:linear-gradient(#d8cdb8,#a89c88)"></div>
    <div class="thumb" role="img" aria-label="Vorschaubild: Eventszene" style="background:linear-gradient(#7a5a3a,#3a2818)"></div>
    <div class="thumb" role="img" aria-label="Vorschaubild: Porträtfoto schwarzweiß" style="background:linear-gradient(#b0b0b0,#404040)"></div>
    <div class="thumb" role="img" aria-label="Vorschaubild: Tischdekoration" style="background:linear-gradient(#3a4a7a,#c8ccd8)"></div>
    <div class="thumb" role="img" aria-label="Vorschaubild: Porträtfoto" style="background:linear-gradient(#a8a4a0,#585450)"></div>
    <div class="thumb" role="img" aria-label="Vorschaubild: Porträtfoto" style="background:linear-gradient(#b08868,#6a4a38)"></div>
    <div class="thumb" role="img" aria-label="Vorschaubild: Porträt mit rotem Hut" style="background:linear-gradient(#b82020,#4a1010)"></div>
    <div class="thumb" role="img" aria-label="Vorschaubild: Porträtfoto" style="background:linear-gradient(#9a8070,#3a2c24)"></div>
    <div class="thumb" role="img" aria-label="Vorschaubild: Porträtfoto" style="background:linear-gradient(#d0ccc8,#7a7470)"></div>
  </div>

  <div class="caption-band"></div>
  <p class="caption">zum vergrössern Bild anklicken / click to enlarge</p>

  <h2 class="page-title">GALERIE / GALLERY</h2>
</body>
</html>
```